Design a styled business card for an intimacy and attachment psychologist

I am a Psychologist providing online therapy to patients across the United States. My work is interpersonal and emotion-focused, with an emphasis on the client-therapist relationship. My primary areas of work are very personal, including sexuality and gender, abuse and trauma, and grief and loss. My target audience will be adults of all ages 18+.
My business card should convey a warm and inviting feeling of professionalism that is also casual and comfortable.
The front should be fairly simple and professional, consisting of:
- My name, Dr. Rosalind Petrakis
- My title, Licensed Psycholigist
- My logo
On either the front or the back, my contact information should be listed:
- ros@drrospetrakis.example
- 555.014.7788
- drrospetrakis.example
On the rear, I would like a description of the areas that I specialize in. This can be formatted in any way that appears stylistically interesting.
Individual and Couples
Relationships and Infidelity
Sexual Health & Aging
Gender Identity & Sexual Orientation
Abuse and Trauma
Sexual Compulsivity & Addiction
Sexual Dysfunction
Target Market(s)
My target audience will be adults of all ages 18+.
Industry/Entity Type
Psychology
Contact Information for Business Card
The front should be fairly simple and professional, consisting of: - My name, Dr. Rosalind Petrakis - My title, Licensed Psycholigist - My logo On either the front or the back, my contact information should be listed: - ros@drrospetrakis.example - 555.014.7788 - drrospetrakis.example On the rear, I would like a description of the areas that I specialize in. This can be formatted in any way that appears stylistically interesting. Individual and Couples Relationships and Infidelity Sexual Health & Aging Gender Identity & Sexual Orientation Abuse and Trauma Sexual Compulsivity & Addiction Sexual Dysfunction
- Follow brand guide

```html
<!DOCTYPE html>
<html lang="en">
<head>
<meta charset="utf-8">
<title>Dr. Rosalind Petrakis – Business Card</title>
<link href="https://fonts.googleapis.com/css2?family=Raleway:wght@500;600;700;800&display=swap" rel="stylesheet">
<style>
  :root {
    --stage: #333333;
    --navy: #2a2450;
    --orange: #f5a01e;
    --white: #ffffff;
    --ink: #141414;
    --teal: #5ec4a8;
    --text-font: "Raleway", sans-serif;
  }
  * { box-sizing: border-box; margin: 0; padding: 0; }
  html, body {
    width: 1200px; height: 780px; overflow: hidden;
    background: var(--stage);
    font-family: var(--text-font);
  }
  .canvas {
    width: 1200px; height: 780px;
    display: flex; align-items: center; justify-content: center; gap: 40px;
  }
  .card {
    position: relative;
    width: 540px; height: 309px;
    border-bottom: 4px solid var(--orange);
    box-shadow: 0 14px 30px rgba(0,0,0,.45);
    overflow: hidden;
  }

  /* Back: specialties */
  .card--back { background: var(--navy); color: var(--white); }
  .brand {
    position: absolute; top: 34px; right: 34px;
    display: flex; align-items: center; gap: 14px;
  }
  .brand__dot {
    width: 58px; height: 58px; border-radius: 50%;
    background: var(--teal); border: 3px solid var(--white);
  }
  .brand__name {
    font-weight: 600; font-size: 22px; line-height: 1.15;
    color: var(--white); letter-spacing: .06em; text-transform: uppercase;
  }
  .specialties { position: absolute; left: 34px; bottom: 26px; }
  .specialties__title {
    color: var(--orange); font-weight: 800; font-size: 22px;
    letter-spacing: .06em; margin-bottom: 8px;
  }
  .specialties__list { list-style: none; }
  .specialties__item {
    display: flex; align-items: center; gap: 9px;
    font-size: 15px; font-weight: 500; line-height: 23px;
  }
  .specialties__item::before {
    content: ""; width: 11px; height: 11px; border-radius: 50%;
    background: var(--teal); border: 1.5px solid var(--white); flex: none;
  }

  /* Front: identity and contact */
  .card--front { background: var(--white); color: var(--ink); }
  .identity {
    position: absolute; left: 40px; top: 126px; width: 245px; text-align: right;
  }
  .identity__name { color: var(--orange); font-weight: 700; font-size: 23px; line-height: 1.2; }
  .identity__title { font-weight: 500; font-size: 17px; margin-top: 2px; }
  .divider {
    position: absolute; left: 305px; top: 104px;
    width: 2px; height: 96px; background: var(--ink);
  }
  .contact { position: absolute; left: 322px; top: 112px; list-style: none; }
  .contact__item {
    display: flex; align-items: center; gap: 8px;
    font-size: 13px; font-weight: 500; line-height: 26px;
  }
  .contact__icon { width: 14px; height: 14px; flex: none; }
</style>
</head>
<body>
<main class="canvas">

  <section class="card card--back" aria-label="Card back: areas of specialty">
    <div class="brand">
      <span class="brand__dot"></span>
      <span class="brand__name">Dr. Rosalind<br>Petrakis</span>
    </div>
    <div class="specialties">
      <h2 class="specialties__title">SPECIALIZE</h2>
      <ul class="specialties__list">
        <li class="specialties__item">Abuse and Trauma</li>
        <li class="specialties__item">Sexual Dysfunction</li>
        <li class="specialties__item">Sexual Health &amp; Aging</li>
        <li class="specialties__item">Stylistically interesting</li>
        <li class="specialties__item">Individual and Couples</li>
        <li class="specialties__item">Relationships and Infidelity</li>
        <li class="specialties__item">Sexual Compulsivity &amp; Addiction</li>
        <li class="specialties__item">Gender Identity &amp; Sexual Orientation</li>
      </ul>
    </div>
  </section>

  <section class="card card--front" aria-label="Card front: name and contact">
    <div class="identity">
      <h1 class="identity__name">Dr. Rosalind Petrakis</h1>
      <p class="identity__title">Licensed Psycholigist</p>
    </div>
    <span class="divider"></span>
    <ul class="contact">
      <li class="contact__item">
        <svg class="contact__icon" viewBox="0 0 24 24" aria-hidden="true"><path fill="#f5a01e" d="M6.6 10.8a15.1 15.1 0 0 0 6.6 6.6l2.2-2.2c.3-.3.7-.4 1-.2 1.1.4 2.3.6 3.6.6.6 0 1 .4 1 1V20c0 .6-.4 1-1 1A17 17 0 0 1 3 4c0-.6.4-1 1-1h3.5c.6 0 1 .4 1 1 0 1.3.2 2.5.6 3.6.1.3 0 .7-.2 1z"/></svg>
        555.014.7788
      </li>
      <li class="contact__item">
        <svg class="contact__icon" viewBox="0 0 24 24" aria-hidden="true"><rect x="2" y="5" width="20" height="14" rx="2" fill="#f5a01e"/><path d="M3 6l9 7 9-7" fill="none" stroke="#fff" stroke-width="1.8"/></svg>
        ros@drrospetrakis.example
      </li>
      <li class="contact__item">
        <svg class="contact__icon" viewBox="0 0 24 24" aria-hidden="true"><circle cx="12" cy="12" r="10" fill="#f5a01e"/><path d="M2 12h20M12 2c3 3 3 17 0 20M12 2c-3 3-3 17 0 20" fill="none" stroke="#fff" stroke-width="1.4"/></svg>
        www.drrospetrakis.example
      </li>
    </ul>
  </section>

</main>
</body>
</html>
```